Album art cover

Album art design concept, my band will be releasing a 11 song rock album in the next few Months. We will be using it as a CD cover, poster, online art cover, maybe even Vinyl. Working album titles are "Copper in the rain" (Preferred album title) or "A lantern under the tide". Anything abstract, painting-like design, or whatever type of design that comes to mind. Fonts are designers choice. Thank You

Target Market(s)

Music business

Colors

Designer to choose colors to be used in the design.

Requirements
Must have
• Our band logo
Nice to have
• Anything abstract, attractive painting type, maybe even some kind of a futuristic design.
Should not have
• Skulls, blood-like, scary designs, nudity, emo type of design

```html
<!DOCTYPE html>
<html lang="en">
<head>
<meta charset="utf-8">
<title>A lantern under the tide — Hollow Bell</title>
<link rel="stylesheet" href="https://fonts.googleapis.com/css2?family=Saira:wght@600;700&display=swap">
<style>
  :root {
    --backdrop: #262626;
    --night-navy: #16252e;
    --deep-teal: #1d3440;
    --snow-haze: #c9d3df;
    --steel-blue: #5c7385;
    --neon-pink: #d9336e;
    --neon-red: #e0443a;
    --title-red: #e8322d;
    --band-white: #f4f4f4;
  }
  html, body {
    margin: 0;
    padding: 0;
    width: 1200px;
    height: 764px;
    overflow: hidden;
    background: var(--backdrop);
  }
  .album-cover {
    position: absolute;
    left: 296px;
    top: 78px;
    width: 608px;
    height: 608px;
    overflow: hidden;
    background: var(--night-navy);
  }
  .cover-photo {
    position: absolute;
    inset: 0;
    background:
      radial-gradient(ellipse 40% 45% at 82% 28%, rgba(217, 51, 110, 0.75), transparent 70%),
      radial-gradient(ellipse 18% 30% at 66% 22%, rgba(224, 68, 58, 0.7), transparent 70%),
      radial-gradient(ellipse 30% 25% at 20% 35%, rgba(200, 60, 70, 0.35), transparent 70%),
      linear-gradient(180deg,
        var(--snow-haze) 0%,
        var(--steel-blue) 30%,
        var(--deep-teal) 52%,
        var(--night-navy) 75%,
        var(--night-navy) 100%);
  }
  .album-title {
    position: absolute;
    right: 364px;
    top: 304px;
    margin: 0;
    font-family: "Saira", sans-serif;
    font-weight: 700;
    font-size: 15px;
    line-height: 18px;
    letter-spacing: 0.16em;
    text-transform: uppercase;
    text-align: right;
    color: var(--title-red);
  }
  .band-name {
    position: absolute;
    right: 36px;
    top: 516px;
    margin: 0;
    font-family: "Saira", sans-serif;
    font-weight: 600;
    font-size: 30px;
    line-height: 32px;
    letter-spacing: 0.04em;
    text-transform: uppercase;
    text-align: right;
    color: var(--band-white);
  }
</style>
</head>
<body>
  <main class="album-cover">
    <div class="cover-photo" role="img" aria-label="Photograph of a snowy city street at night, crowds with umbrellas under tall buildings and glowing pink and red billboards"></div>
    <h1 class="album-title">A lantern<br>under the tide</h1>
    <p class="band-name">Hollow<br>Bell</p>
  </main>
</body>
</html>
```